Business and Success Coaching Business Card

Need a business card for my coaching business. I coach small businesses, career professionals and, individuals wanting to unlock their human potential and achieve excellence. At the heart of our methodology is the Shaping Purposeful Action Routines Knowingly (SPARK) approach to formulate empowerment, create principles for success and setting achievable outcomes. I would like something that incorporates our new logo, something clean and sharp with a solid darker, but complementary background, color on the card front. The back should be white where there will be room for three questions

Target Market(s)

People looking to advance and improve themselves through a success coach

Industry/Entity Type

Life Coaching

Contact Information for Business Card

Contact information on card.
Business name on front of card
Questions on back

Font styles to use
Other font styles liked:
• Century Gothic or other Serif style fonts that look similar to Century Gothic

Colors

Designer to choose colors to be used in the design.

Requirements
Must have
• Logo on front of card
• Business name - The Steady Forge
• Contact name - Ted Harlow
• Address - Box 4619, Littleton, CO 80127-4619
• Phone number - 303-555-0147
• Email address - harlow.ted@thesteadyforge.example
• Certifications - CSC, CCHt, PTT, PNLP
• Back of card
• Three questions on the back of the card:
• If you were at your best, what would you do right now?
• What is the decision you have been avoiding?
• What's one action you could take in the next 10 minutes?
Nice to have
• I would like to see a solid color on the front of the card that compliments the logo.
• Back should be white, or could be contrasting, but need to have the three questions.

```html
<!DOCTYPE html>
<html lang="en">
<head>
<meta charset="utf-8">
<title>The Steady Forge – Business Card</title>
<link rel="stylesheet" href="https://fonts.googleapis.com/css2?family=Open+Sans:wght@300;400;700&display=swap">
<style>
  :root {
    --bg-top: #6f40d8;
    --bg-mid: #9270e2;
    --bg-low: #3d12b0;
    --bg-bottom: #23029b;
    --front-green: #52dc6e;
    --back-paper: #eaefe8;
    --navy: #0b1f9c;
    --icon-chip: #d8e6f4;
    --white: #ffffff;
    --soft-white: #eef6f0;
    --question-green: #4fd96c;
  }
  * { box-sizing: border-box; margin: 0; padding: 0; }
  html, body { width: 1154px; height: 1200px; overflow: hidden; }
  body {
    position: relative;
    font-family: "Open Sans", Arial, sans-serif;
    background: linear-gradient(180deg, var(--bg-top) 0%, var(--bg-top) 30%, var(--bg-mid) 47%, var(--bg-low) 58%, var(--bg-bottom) 75%, var(--bg-bottom) 100%);
  }

  .card {
    position: absolute;
    width: 481px;
    height: 842px;
    box-shadow: 0 30px 24px -18px rgba(20, 5, 60, 0.55);
  }
  .card--front { left: 64px; top: 83px; background: var(--front-green); }
  .card--back  { left: 626px; top: 77px; background: var(--back-paper); }

  .centered { position: absolute; left: 0; width: 100%; text-align: center; white-space: nowrap; }

  /* front brand block */
  .brand-mark {
    position: absolute; left: 50%; top: 68px;
    width: 96px; height: 96px; margin-left: -48px;
    border-radius: 50%; background: var(--navy);
  }
  .brand-name {
    top: 185px; font-size: 35px; line-height: 44px; font-weight: 700;
    color: var(--navy); letter-spacing: -0.3px;
  }

  .company-line { top: 372px; font-size: 26px; line-height: 32px; font-weight: 300; color: var(--soft-white); }
  .rule {
    position: absolute; left: 50%; height: 2px;
    background: linear-gradient(90deg, rgba(255,255,255,0), rgba(225,255,235,0.9), rgba(255,255,255,0));
  }
  .person-name { top: 412px; font-size: 24px; line-height: 30px; font-weight: 300; color: var(--soft-white); }
  .credentials { top: 442px; font-size: 12px; line-height: 16px; font-weight: 400; color: var(--soft-white); }

  .contact-icon {
    position: absolute; left: 50%; width: 24px; height: 24px; margin-left: -12px;
    border-radius: 50%; background: var(--icon-chip);
  }
  .contact-icon svg { display: block; width: 24px; height: 24px; }
  .contact-text { font-size: 18px; line-height: 24px; font-weight: 300; color: var(--soft-white); letter-spacing: 0.2px; }

  /* back */
  .idea-art {
    position: absolute; left: 156px; top: 420px; width: 168px; height: 248px;
    border-radius: 84px 84px 40px 40px;
    background: radial-gradient(circle at 50% 35%, rgba(82,220,110,0.16), rgba(82,220,110,0.04) 70%);
  }
  .idea-name {
    top: 504px; font-size: 14px; line-height: 20px; font-weight: 700; color: var(--question-green);
  }
  .question { font-size: 15px; line-height: 20px; font-weight: 300; color: var(--question-green); }

  /* presentation brand below */
  .showcase-mark {
    position: absolute; left: 277px; top: 1018px; width: 50px; height: 50px;
    border-radius: 50%; background: var(--back-paper);
  }
  .showcase-name {
    position: absolute; left: 152px; width: 300px; top: 1092px; text-align: center;
    font-size: 21px; line-height: 28px; font-weight: 700; color: var(--white);
  }
</style>
</head>
<body>

<section class="card card--front" aria-label="Card front">
  <div class="brand-mark" aria-hidden="true"></div>
  <p class="centered brand-name">The Steady Forge</p>

  <p class="centered company-line">The Steady Forge</p>
  <div class="rule" style="top:407px;width:180px;margin-left:-90px;"></div>
  <p class="centered person-name">TED HARLOW</p>
  <p class="centered credentials">CSC, CCHt, PTT, PNLP</p>

  <div class="contact-icon" style="top:499px;">
    <svg viewBox="0 0 24 24" aria-hidden="true"><path d="M8.2 6.5c.4-.4 1-.4 1.3 0l1.3 1.6c.3.4.3.9-.1 1.2l-.8.7c.6 1.3 1.6 2.3 2.9 2.9l.7-.8c.3-.4.8-.4 1.2-.1l1.6 1.3c.4.3.4.9 0 1.3l-.9.9c-.6.6-1.5.8-2.3.4-2.4-1.1-4.3-3-5.4-5.4-.4-.8-.2-1.7.4-2.3z" fill="var(--navy)"/></svg>
  </div>
  <p class="centered contact-text" style="top:527px;">303-555-0147</p>
  <div class="rule" style="top:560px;width:240px;margin-left:-120px;"></div>

  <div class="contact-icon" style="top:573px;">
    <svg viewBox="0 0 24 24" aria-hidden="true"><path d="M12 5.5a4.3 4.3 0 0 0-4.3 4.3c0 3.2 4.3 7.7 4.3 7.7s4.3-4.5 4.3-7.7A4.3 4.3 0 0 0 12 5.5z" fill="none" stroke="var(--navy)" stroke-width="1.6"/><circle cx="12" cy="9.8" r="1.5" fill="var(--navy)"/></svg>
  </div>
  <p class="centered contact-text" style="top:599px;">Box 4619, Littleton, CO 80127-4619</p>
  <div class="rule" style="top:634px;width:240px;margin-left:-120px;"></div>

  <div class="contact-icon" style="top:647px;">
    <svg viewBox="0 0 24 24" aria-hidden="true"><path d="M12 6.5c3.3 0 5.8 2 5.8 4.6s-2.5 4.6-5.8 4.6c-.6 0-1.2-.1-1.7-.2L7.6 17l.9-2.4c-1.4-.9-2.3-2.1-2.3-3.5 0-2.6 2.5-4.6 5.8-4.6z" fill="var(--navy)"/><circle cx="9.6" cy="11.1" r=".8" fill="var(--icon-chip)"/><circle cx="12" cy="11.1" r=".8" fill="var(--icon-chip)"/><circle cx="14.4" cy="11.1" r=".8" fill="var(--icon-chip)"/></svg>
  </div>
  <p class="centered contact-text" style="top:673px;">harlow.ted@thesteadyforge.example</p>
  <div class="rule" style="top:708px;width:240px;margin-left:-120px;"></div>

  <div class="contact-icon" style="top:721px;">
    <svg viewBox="0 0 24 24" aria-hidden="true"><circle cx="12" cy="12" r="6" fill="var(--navy)"/><path d="M6 12h12M12 6v12M8 8.5c2.4 1 5.6 1 8 0M8 15.5c2.4-1 5.6-1 8 0" stroke="var(--icon-chip)" stroke-width=".8" fill="none"/></svg>
  </div>
  <p class="centered contact-text" style="top:749px;">www.thesteadyforge.example</p>
</section>

<section class="card card--back" aria-label="Card back">
  <div class="idea-art" role="img" aria-label="Thin green outline of a light bulb framing the brand name"></div>
  <p class="centered idea-name">The Steady Forge</p>

  <p class="centered question" style="top:697px;">If you were at your best, what would you do right now?</p>
  <p class="centered question" style="top:733px;">What is the decision you have been avoiding?</p>
  <p class="centered question" style="top:768px;">What's one action you could take in the next 10 minutes?</p>
  <div class="rule" style="top:795px;width:180px;margin-left:-90px;background:linear-gradient(90deg,rgba(79,217,108,0),var(--question-green),rgba(79,217,108,0));"></div>
</section>

<div class="showcase-mark" aria-hidden="true"></div>
<p class="showcase-name">The Steady Forge</p>

</body>
</html>
```